my website is tabellepiece.com. (brand name is ta belle pièce) This is just a template that i have choose for. The content and the pictures are not about my business just the template.
I would like to have 4 pages for now. 1 homepage, which will be an overview for all pages, it is right now in this way. It will directly highlight my story. My website will tell an exclusive story about details which makes the difference and will make people happy with very small things. It will be art related but very stylish as well. I also want to have a event agenda on my homepage where people can see where my next event is. Page 2 my blog, where I will write weekly about mindset, lifestyle and details. Inspiration place for people who are looking for unique and exclusive approaches in life. Page 3 shop, where I will sell my stuff which is handmade and unique, it will be limited edition stuff. Mostly I will make the designs from marbling art, which I am a teacher for. (https://www.vidorastream.com/watch?v=Kq7TbWm2Xa) check this video out for more. Page 4 is book page. Here people will be able to book private or group classes for marbling art (check the video). I have already a community of more than 500 people on join ring, which will be my public as well. I wanna implement the join ring button on this page as well. to be able to track.

This is about my website. I also need a logo for my brand, which will suit my website and my goals.

I can also give you a reference website, which really like as structure and style;
https://www.brightmorrowco.com/products/the-daybook-organizer?ref=Xp4RtLm8QzVw2NbKc7HsJd9FgTy3MvEqBa6WnUoZr1LkPxYhGiCe5DsAtQfVbNj0HmRwKyXo8LcTpZaEsUv2GqDnIwMb

ta belle pièce

4 page

• I can also give you a reference website, which really like as structure and style;
• https://www.brightmorrowco.com/products/the-daybook-organizer?ref=Xp4RtLm8QzVw2NbKc7HsJd9FgTy3MvEqBa6WnUoZr1LkPxYhGiCe5DsAtQfVbNj0HmRwKyXo8LcTpZaEsUv2GqDnIwMb

```html
<!DOCTYPE html>
<html lang="en">
<head>
<meta charset="utf-8">
<title>ta belle pièce — Home</title>
<link rel="stylesheet" href="https://fonts.googleapis.com/css2?family=Josefin+Sans:wght@400;600&family=Playfair+Display:wght@700&family=Yesteryear&display=swap">
<style>
  :root {
    --ink: #141414;
    --paper: #ffffff;
    --muted: #8a8a8a;
    --line: #cfcfcf;
    --card: #f3efec;
    --band: #ececea;
    --cream: #f4ede5;
    --footer: #111111;
    --dark: #232323;
  }
  * { box-sizing: border-box; margin: 0; padding: 0; }
  html, body { width: 1200px; height: 2821px; overflow: hidden; background: var(--paper); }
  body { font-family: "Josefin Sans", sans-serif; color: var(--ink); }
  .page { position: relative; width: 1200px; height: 2821px; overflow: hidden; }
  .abs { position: absolute; }
  .script { font-family: "Yesteryear", cursive; font-weight: 400; color: var(--ink); }

  /* Header */
  .nav-link { position: absolute; top: 26px; font-size: 14px; letter-spacing: 2px; }
  .brand { position: absolute; left: 536px; top: 12px; display: flex; align-items: center; gap: 10px; }
  .brand-mark { width: 34px; height: 34px; border: 1.5px solid var(--ink); border-radius: 50%; }
  .brand-name { font-size: 17px; font-weight: 600; line-height: 1; }
  .social-dot { position: absolute; top: 26px; width: 12px; height: 12px; border-radius: 50%; background: var(--ink); }

  /* Hero */
  .hero-art-left { left: 0; top: 75px; width: 640px; height: 448px; background: linear-gradient(120deg, #8d8c8a 0%, #a9a8a5 45%, #bdbcb8 100%); z-index: 2; }
  .hero-art-right { left: 564px; top: 75px; width: 636px; height: 517px; background: radial-gradient(circle at 40% 60%, #8f6f95 0%, #6e4e5c 35%, #4c3b35 70%, #6b5a3c 100%); z-index: 1; }
  .hero-card { left: 301px; top: 201px; width: 596px; height: 250px; background: var(--paper); z-index: 3; text-align: center; }
  .hero-kicker { font-size: 42px; line-height: 1; margin-top: 16px; }
  .hero-title { font-size: 64px; line-height: 1; margin-top: 2px; }
  .hero-copy { font-size: 13px; line-height: 19px; width: 540px; margin: 10px auto 0; }
  .hero-cta { font-size: 16px; margin-top: 14px; letter-spacing: .5px; }

  /* Products */
  .product { top: 668px; width: 237px; height: 380px; }
  .product.is-active { background: var(--paper); box-shadow: 0 4px 18px rgba(0,0,0,.14); }
  .product-name { position: absolute; top: 60px; left: 22px; font-family: "Playfair Display", serif; font-size: 16px; }
  .product-stage { position: absolute; left: 0; top: 135px; width: 237px; height: 245px; background: var(--card); }
  .next-btn { position: absolute; top: 113px; right: 15px; width: 41px; height: 41px; background: var(--ink); }
  .badge { position: absolute; top: 135px; left: 0; padding: 0 14px; height: 26px; line-height: 27px; background: var(--dark); color: #fff; font-size: 11px; }
  .price { position: absolute; top: 336px; right: 15px; width: 103px; height: 29px; line-height: 30px; background: var(--dark); color: #fff; font-size: 12px; text-align: center; }
  .quick-view { position: absolute; left: 0; top: 239px; width: 237px; height: 37px; line-height: 39px; background: rgba(255,255,255,.85); text-align: center; font-size: 16px; }
  .pager { top: 984px; font-size: 16px; font-weight: 600; }
  .pager-ring { left: 118px; top: 976px; width: 34px; height: 34px; border-radius: 50%; box-shadow: 0 1px 6px rgba(0,0,0,.12); }

  /* Origins */
  .origins-band { left: 0; top: 1125px; width: 1200px; height: 446px; background: linear-gradient(90deg, #dcdcda 0%, var(--band) 55%, #efefee 100%); }
  .origins-title { left: 113px; top: 1190px; font-size: 64px; }
  .origins-rule { left: 0; top: 1228px; width: 108px; height: 1px; background: var(--ink); }
  .origins-copy { left: 113px; top: 1284px; width: 455px; font-size: 12.5px; line-height: 25px; }
  .photo-studio { left: 525px; top: 1386px; width: 434px; height: 264px; background: linear-gradient(160deg, #9a9a98 0%, #2a2a2a 40%, #151515 100%); }
  .photo-ribbons { left: 675px; top: 1198px; width: 412px; height: 286px; background: linear-gradient(135deg, #f2f2f2 0%, #e4e4e4 55%, #cbbfa9 100%); }

  /* Agenda / journal */
  .post-title { font-size: 16px; letter-spacing: .3px; white-space: nowrap; }
  .post-date { font-size: 13px; color: #bdbdbd; writing-mode: vertical-rl; letter-spacing: 1px; }
  .post-one { left: 307px; top: 1796px; width: 287px; height: 439px; background: linear-gradient(180deg, #f7f7f7 0%, #ececec 55%, #f6f6f6 100%); box-shadow: 0 2px 10px rgba(0,0,0,.08); z-index: 2; }
  .post-one-shadow { left: 594px; top: 1874px; width: 76px; height: 286px; background: #efefef; }
  .post-two { left: 758px; top: 1723px; width: 136px; height: 211px; background: linear-gradient(180deg, #5e6a5a 0%, #87a37f 55%, #4a4a48 100%); }
  .post-three { left: 758px; top: 2009px; width: 136px; height: 205px; background: linear-gradient(180deg, #f2f2f0 0%, #e8ebe7 55%, #9fcbc0 80%, #e9e6e2 100%); }
  .thumb-a { left: 156px; top: 2024px; width: 98px; height: 98px; background: linear-gradient(135deg, #b7a08f, #d9c9c2); }
  .thumb-b { left: 946px; top: 1798px; width: 98px; height: 98px; background: linear-gradient(135deg, #ead6d0, #f3e6e2); }

  /* Subscribe */
  .subscribe-band { left: 0; top: 2323px; width: 1200px; height: 284px; background: var(--cream); }
  .subscribe-title { left: 0; top: 2372px; width: 1200px; text-align: center; font-size: 60px; }
  .subscribe-sub { left: 0; top: 2448px; width: 1200px; text-align: center; font-size: 14px; }
  .field { top: 2506px; height: 27px; border-bottom: 1px solid var(--line); font-size: 11px; padding-left: 6px; }
  .submit { left: 766px; top: 2496px; width: 137px; height: 38px; line-height: 40px; background: var(--ink); color: #fff; text-align: center; font-size: 16px; }

  /* Footer */
  .footer { left: 0; top: 2607px; width: 1200px; height: 214px; background: var(--footer); color: #fff; }
  .footer-circle { position: absolute; top: 43px; width: 38px; height: 38px; border-radius: 50%; border: 1px solid #bbb; }
  .footer-circle.is-filled { background: #fff; border-color: #fff; }
  .footer-links { position: absolute; top: 111px; left: 0; width: 1200px; text-align: center; font-size: 11px; word-spacing: 2px; }
  .footer-links span { margin: 0 26px; }
  .footer-rule { position: absolute; left: 150px; top: 160px; width: 900px; height: 1px; background: #333; }
  .copyright { position: absolute; top: 181px; left: 0; width: 1200px; text-align: center; font-size: 11px; }
</style>
</head>
<body>
<div class="page">

  <header>
    <span class="nav-link" style="left:245px">Home</span>
    <span class="nav-link" style="left:368px">Shop</span>
    <div class="brand"><span class="brand-mark"></span><span class="brand-name">ta belle pièce</span></div>
    <span class="nav-link" style="left:737px">Book Online</span>
    <span class="nav-link" style="left:918px">Blog</span>
    <span class="social-dot" style="left:1008px"></span>
    <span class="social-dot" style="left:1030px"></span>
    <svg class="abs" style="left:1062px;top:16px" width="28" height="28" viewBox="0 0 28 28" fill="none" stroke="#141414" stroke-width="1.4">
      <path d="M3 6h4l3 13h13l3-9H9"/><circle cx="12" cy="23" r="1.6"/><circle cx="21" cy="23" r="1.6"/>
    </svg>
  </header>

  <section class="hero">
    <div class="abs hero-art-right" role="img" aria-label="Close-up of colourful marbling paint swirls with brushes"></div>
    <div class="abs hero-art-left" role="img" aria-label="Artist at work beside a white plinth against a grey wall"></div>
    <div class="abs hero-card">
      <p class="script hero-kicker">Our New</p>
      <h1 class="script hero-title">Arrivals Are Here</h1>
      <p class="hero-copy">ta belle pièce is a leading Online Store. We provide an unparalleled selection of the very best quality products, an easy and comfortable shopping experience, expedited shipping offers, and exceptional customer service. Check out our collection of new arrivals, best-sellers, and clearance items today.</p>
      <p class="hero-cta">Shop Now »</p>
    </div>
  </section>

  <section class="products">
    <div class="abs" style="left:0;top:995px;width:117px;height:1px;background:var(--line)"></div>
    <div class="abs pager-ring"></div>
    <span class="abs pager" style="left:130px">1</span>
    <span class="abs pager" style="left:165px">2</span>
    <span class="abs pager" style="left:192px">3</span>
    <div class="abs" style="left:218px;top:992px;width:40px;height:2px;background:var(--ink)"></div>
    <div class="abs" style="left:262px;top:992px;width:12px;height:2px;background:var(--ink)"></div>

    <article class="abs product" style="left:310px">
      <h3 class="product-name">I'm a Product</h3>
      <div class="product-stage" role="img" aria-label="Product image of a handmade marbled piece"></div>
      <span class="badge">Best Seller</span>
      <span class="next-btn"><svg width="41" height="41" viewBox="0 0 41 41"><path d="M18 15l6 5.5-6 5.5" stroke="#fff" stroke-width="1.6" fill="none"/></svg></span>
      <span class="price">€ 10.00</span>
    </article>

    <article class="abs product is-active" style="left:572px">
      <h3 class="product-name">I'm a Product</h3>
      <div class="product-stage" role="img" aria-label="Product image of a limited edition marbled piece"></div>
      <span class="quick-view">Quick View</span>
      <span class="next-btn"><svg width="41" height="41" viewBox="0 0 41 41"><path d="M18 15l6 5.5-6 5.5" stroke="#fff" stroke-width="1.6" fill="none"/></svg></span>
      <span class="price">€ 15.00</span>
    </article>

    <article class="abs product" style="left:833px">
      <h3 class="product-name">I'm a Product</h3>
      <div class="product-stage" role="img" aria-label="Product image of a new marbled piece"></div>
      <span class="badge">New</span>
      <span class="next-btn"><svg width="41" height="41" viewBox="0 0 41 41"><path d="M18 15l6 5.5-6 5.5" stroke="#fff" stroke-width="1.6" fill="none"/></svg></span>
      <span class="price">€ 120.00</span>
    </article>

    <article class="abs product" style="left:1095px">
      <h3 class="product-name">I'm a Product</h3>
      <div class="product-stage" role="img" aria-label="Product image"></div>
    </article>
  </section>

  <section class="origins">
    <div class="abs origins-band" role="img" aria-label="Faded studio backdrop with marbling tools"></div>
    <div class="abs origins-rule"></div>
    <h2 class="abs script origins-title">Origins</h2>
    <p class="abs origins-copy">ta belle pièce is a story about details, the small things that make the difference and make people happy. Every piece begins in the studio as marbling art, floated by hand on water and printed once, so no two are alike. Each design is made in a limited edition, art that is stylish enough to live with every day.</p>
    <div class="abs photo-studio" role="img" aria-label="Dark marbling tray filled with ink"></div>
    <div class="abs photo-ribbons" role="img" aria-label="Wrapped gift with ribbon spools on a white table"></div>
  </section>

  <section class="agenda" aria-label="Event agenda">
    <p class="abs post-title" style="left:506px;top:1768px">Next event: open studio</p>
    <span class="abs post-date" style="left:284px;top:1796px">May 9, 2016</span>
    <div class="abs post-one-shadow"></div>
    <div class="abs post-one" role="img" aria-label="Event image for the open studio"></div>
    <div class="abs thumb-a" role="img" aria-label="Small marbled paper detail"></div>

    <div class="abs post-two" role="img" aria-label="Event image for a private marbling class"></div>
    <span class="abs post-date" style="left:732px;top:1858px">May 9, 2016</span>
    <p class="abs post-title" style="left:809px;top:1942px">Private marbling class</p>
    <div class="abs thumb-b" role="img" aria-label="Small pale pink marbled texture"></div>

    <div class="abs post-three" role="img" aria-label="Event image for a group marbling workshop"></div>
    <span class="abs post-date" style="left:900px;top:2136px">May 9, 2016</span>
    <p class="abs post-title" style="left:672px;top:2229px">Group marbling workshop</p>
  </section>

  <section class="subscribe">
    <div class="abs subscribe-band"></div>
    <h2 class="abs script subscribe-title">Subscribe</h2>
    <p class="abs subscribe-sub">Stay up to date</p>
    <div class="abs field" style="left:295px;width:198px">First name</div>
    <div class="abs field" style="left:532px;width:196px">Email Address</div>
    <div class="abs submit">Submit</div>
  </section>

  <footer class="abs footer">
    <span class="footer-circle" style="left:510px"></span>
    <span class="footer-circle is-filled" style="left:557px"></span>
    <span class="footer-circle" style="left:605px"></span>
    <span class="footer-circle" style="left:653px"></span>
    <p class="footer-links"><span>Home</span>|<span>Shop</span>|<span>Book Online</span>|<span>Blog</span></p>
    <div class="footer-rule"></div>
    <p class="copyright">Copyright © 2017 TABELLEPIECE Inc. All Rights Reserved.</p>
  </footer>

</div>
</body>
</html>
```